Modern Brochure Design for Music School !!

I would like to have a brochure (A4 two fold) created for my partners music school. I would like it to incorporate information from his website, showing what classes are taught (singing lessons, drum lessons, guitar lessons and keyboard lessons). I would like to keep the same font style or as close to what's on the website if possible.

It needs to grab attention and be modern in design to attract age group of 18-35 while briefly detailing what services they provide, including their location and phone number

Info can all be found on the website www.themelodyloft.com.au

Target Market(s)

18-35 y/o

Industry/Entity Type

School

Font styles to use
Serif

Colors
000000

Requirements
Must have
• Key content from website
• List of classes (singing, drums, guitar, keyboard)
• Address / phone number
• Find us on Facebook - The Melody Loft /Instagram @the_melody_loft
• Mention - gift vouchers available
• Black and white colours preferably no bright colours (like website)
• Modern and professional please!!
Nice to have
• Same type font as website or close to
• Not too much content
Should not have
• .

```html
<!DOCTYPE html>
<html lang="en">
<head>
<meta charset="utf-8">
<title>The Melody Loft – Brochure Spread</title>
<link href="https://fonts.googleapis.com/css2?family=Exo+2:wght@300;400;600;700&family=Open+Sans:wght@400;600&display=swap" rel="stylesheet">
<style>
  :root {
    --backdrop: #dcdbd7;
    --page-top: #222222;
    --page-bottom: #0b0b0b;
    --band: #6a6a6a;
    --band-light: #8a8a8a;
    --text-main: #e6e6e6;
    --text-soft: #b9b9b9;
    --text-dim: #9a9a9a;
    --white: #ffffff;
  }
  * { box-sizing: border-box; margin: 0; padding: 0; }
  html, body {
    width: 1200px; height: 804px; overflow: hidden;
    background: var(--backdrop);
  }
  .spread {
    position: absolute; left: 60px; top: 20px;
    width: 1080px; height: 764px;
    display: flex;
    box-shadow: 0 10px 30px rgba(0,0,0,.25);
  }
  .page {
    position: relative; width: 540px; height: 764px;
    background: linear-gradient(170deg, var(--page-top) 0%, var(--page-bottom) 70%);
    overflow: hidden;
  }
  .page--left { border-right: 1px solid #000; }
  .page-shapes { position: absolute; inset: 0; }
  .tagline {
    position: absolute; font-family: "Exo 2", sans-serif; font-weight: 400;
    text-transform: uppercase; font-size: 11px; line-height: 1.3;
    color: var(--text-soft); letter-spacing: .3px;
  }
  .heading {
    position: absolute; font-family: "Exo 2", sans-serif; font-weight: 600;
    color: var(--white); text-transform: uppercase; line-height: 1.15;
  }
  .body-copy {
    position: absolute; font-family: "Open Sans", sans-serif;
    color: var(--text-main);
  }
  .body-copy p + p { margin-top: 9px; }
  .page--left .body-copy { left: 40px; top: 428px; width: 462px; font-size: 9.6px; line-height: 1.45; }
  .page--right .body-copy { left: 40px; top: 368px; width: 470px; font-size: 7.6px; line-height: 1.4; }
  .page--right .body-copy p + p { margin-top: 6px; }
  .available {
    position: absolute; left: 120px; top: 492px; width: 360px; text-align: center;
    font-family: "Exo 2", sans-serif; font-weight: 300; font-size: 20px;
    color: var(--white); text-transform: uppercase;
  }
  .lesson-label {
    position: absolute; font-family: "Exo 2", sans-serif; font-weight: 600;
    font-size: 11px; color: var(--white); text-transform: uppercase;
  }
  .footer-line {
    position: absolute; font-family: "Open Sans", sans-serif; font-size: 8.5px;
    color: var(--text-dim);
  }
  .page-number {
    position: absolute; width: 40px; height: 38px; background: #4a4a4a;
    font-family: "Exo 2", sans-serif; font-size: 17px; color: var(--text-soft);
    display: flex; align-items: center; justify-content: center;
  }
</style>
</head>
<body>
<div class="spread">

  <!-- Page 2 -->
  <section class="page page--left">
    <svg class="page-shapes" width="540" height="764" viewBox="0 0 540 764">
      <defs>
        <linearGradient id="drumTone" x1="0" y1="0" x2="1" y2="1">
          <stop offset="0" stop-color="#5a4a3e"/>
          <stop offset=".5" stop-color="#2e2a28"/>
          <stop offset="1" stop-color="#141414"/>
        </linearGradient>
      </defs>
      <polygon role="img" aria-label="Photo of a drummer playing a kit with cymbals"
        points="30,106 340,106 388,66 510,66 510,330 30,330" fill="url(#drumTone)"/>
      <polyline points="30,103 338,103 386,63 510,63" fill="none" stroke="var(--band)" stroke-width="5"/>
      <polygon points="510,332 510,340 140,340 46,424 34,424 128,332" fill="var(--band)"/>
    </svg>
    <div class="tagline" style="left:40px; top:38px; width:360px;">Pluck up the courage to achieve your dreams and start living life to the beat of your own drum!</div>
    <h2 class="heading" style="left:118px; top:356px; font-size:21px;">We believe that anyone can<br>learn how to sing</h2>
    <div class="body-copy">
      <p>We believe that anyone can learn how to sing, and we pride ourselves on our ability to help students find their own distinct vocal personality. The uniqueness of your voice is part of what makes you special, so we don't believe in teaching you to merely mimic other singers.</p>
      <p>At The Melody Loft, students are given the opportunity to gain valuable live performance and recording skills through the use of professional speaker systems, recording software, mixing desks and microphones. We also hold free concerts throughout the year in order to give our students a chance to build their confidence in performing before an audience, and to give their friends and family a chance to see what they have achieved.</p>
      <p>In each lesson with The Melody Loft, you will work through a song with your teacher. The teacher will then tailor a program of vocal exercises and scales to your individual vocal needs. With each song - some of which will be chosen by you and others will be chosen by your teacher for the purposes of learning a specific technique - you will find both your vocal range and vocal stamina increasing.</p>
      <p>Whether your musical tastes incline towards heavy metal, jazz, pop, rock, R&amp;B or musical theatre, we can teach you how to use the shape of your mouth, your breathing and the volume of your voice to produce the sounds essential to each musical style. We can also teach you to do this each and every time without damaging your voice.</p>
    </div>
    <div class="page-number" style="left:0; top:712px;">2</div>
    <div class="footer-line" style="left:52px; top:726px;">112 Harmony Road Brookvale Victoria &nbsp;|&nbsp; 1300 555 214 &nbsp;|&nbsp; info@themelodyloft.com.au</div>
  </section>

  <!-- Page 3 -->
  <section class="page page--right">
    <svg class="page-shapes" width="540" height="764" viewBox="0 0 540 764">
      <defs>
        <linearGradient id="concertTone" x1="0" y1="0" x2="1" y2="1">
          <stop offset="0" stop-color="#1a2440"/>
          <stop offset=".45" stop-color="#6f86b4"/>
          <stop offset="1" stop-color="#0e1222"/>
        </linearGradient>
        <linearGradient id="keysTone" x1="0" y1="0" x2="1" y2="1">
          <stop offset="0" stop-color="#d8cfc6"/>
          <stop offset="1" stop-color="#6b645e"/>
        </linearGradient>
        <linearGradient id="guitarTone" x1="0" y1="0" x2="1" y2="1">
          <stop offset="0" stop-color="#3a1a14"/>
          <stop offset="1" stop-color="#7a4a30"/>
        </linearGradient>
      </defs>
      <polygon role="img" aria-label="Photo of a crowd with raised hands at a concert under stage lights"
        points="30,92 330,92 380,50 510,50 510,292 30,292" fill="url(#concertTone)"/>
      <polyline points="30,89 328,89 378,47 510,47" fill="none" stroke="var(--band)" stroke-width="5"/>
      <polygon points="510,294 510,302 122,302 42,376 30,376 112,294" fill="var(--band)"/>
      <rect role="img" aria-label="Photo of hands playing a piano keyboard" x="140" y="532" width="155" height="110" fill="url(#keysTone)"/>
      <rect role="img" aria-label="Photo of a guitarist playing an electric guitar" x="301" y="532" width="160" height="110" fill="url(#guitarTone)"/>
      <polygon points="140,642 295,642 295,668 160,668" fill="var(--band-light)"/>
      <polygon points="301,642 470,622 470,632 451,662 301,662" fill="var(--band-light)"/>
    </svg>
    <div class="tagline" style="left:30px; top:28px; width:330px;">Fun and affordable one-on-one vocal tuition and now guitar, drums and keyboard tuition</div>
    <h2 class="heading" style="left:124px; top:312px; font-size:25px;">Lessons</h2>
    <div class="body-copy">
      <p>Lessons with The Melody Loft generally last for 30 minutes, involve one-on-one tuition and are available Monday through Saturday, between the hours of 12pm and 9pm. Saturdays 10am through to 3pm.</p>
      <p>If you require an alternative arrangement, such as group lessons at your home or coaching in the studio while you record that all important demo or EP, we will gladly accommodate such arrangements wherever possible.</p>
      <p>Lessons with Daniel, our Principal Instructor, Monday to Thursday. Lessons with Mara, Tuesdays and Fridays. Theo, is the newest member to The Melody Loft team, teaches Guitar on Mondays, Vocals Monday, Wednesdays and Saturdays.</p>
      <p>Discount rates apply where 10 lessons are paid for in advance, or where a student refers a family member or friend to us. We ask that you bring a USB storage device to each lesson, to which we can save your assigned vocal exercises for practicing at home. If you do not have access to a computer at home, we can put your vocal exercises on a CD instead.</p>
    </div>
    <div class="available">Lessons are available now !</div>
    <div class="lesson-label" style="left:172px; top:650px;">Guitar Lessons</div>
    <div class="lesson-label" style="left:318px; top:642px;">Keyboard Lessons</div>
    <div class="footer-line" style="left:150px; top:690px;">112 Harmony Road Brookvale Victoria &nbsp;|&nbsp; 1300 555 214 &nbsp;|&nbsp; info@themelodyloft.com.au</div>
    <div class="page-number" style="left:500px; top:662px;">3</div>
  </section>

</div>
</body>
</html>
```